Der Designer hat mir ein super Logo entworfen sehr schnell tolle Zusammenarbeit. Ist nur zu empfehlen
Zielgruppe
Es handelt sich um eine Haus und Immobilienverwaltung die Zielgruppe sind Eigentümer der Häuser und Firmen
Aufgabenstellung
Edel klassisch

```html
<!DOCTYPE html>
<html lang="de">
<head>
<meta charset="utf-8">
<title>Halden Gruppe – Visitenkarten</title>
<link href="https://fonts.googleapis.com/css2?family=Arimo:wght@400&display=swap" rel="stylesheet">
<style>
  :root {
    --stage: #4d4d4d;
    --card-dark: #373737;
    --card-light: #ffffff;
    --blue: #7ab0cb;
    --green: #84a898;
    --band-grey: #b3b3b3;
    --mark-grey: #a6a6a6;
    --text: #555555;
    --rule: #d6d6d6;
  }
  html, body {
    margin: 0;
    width: 1200px;
    height: 1200px;
    overflow: hidden;
    background: var(--stage);
    font-family: "Arimo", Arial, sans-serif;
  }
  .sheet { position: relative; width: 1200px; height: 1200px; }

  .card { position: absolute; width: 467px; height: 302px; }
  .card--front { left: 366px; top: 256px; background: var(--card-dark); }
  .card--back { top: 709px; background: var(--card-light); }
  .card--mira { left: 68px; }
  .card--selma { left: 641px; }

  .brand {
    display: flex; align-items: center; gap: 12px;
    position: absolute; left: 0; right: 0; top: 128px;
    justify-content: center;
  }
  .brand__square { width: 22px; height: 22px; background: var(--blue); }
  .brand__name {
    color: var(--mark-grey); font-size: 30px; letter-spacing: 4px;
  }

  .brand--small {
    top: 38px; left: auto; right: 27px; justify-content: flex-end; gap: 8px;
  }
  .brand--small .brand__square { width: 14px; height: 14px; }
  .brand--small .brand__name { font-size: 17px; letter-spacing: 2px; }

  .divider {
    position: absolute; left: 191px; top: 23px; width: 1px; height: 227px;
    background: var(--rule);
  }
  .person {
    position: absolute; left: 0; width: 191px; top: 124px; text-align: center;
  }
  .person__name { color: var(--text); font-size: 21px; margin: 0; }
  .person__role { color: #777; font-size: 10.5px; margin: 5px 0 0; }

  .contact {
    position: absolute; left: 228px; right: 27px; top: 152px;
    color: var(--text); font-size: 13px;
  }
  .contact__address { text-align: right; margin: 0; }
  .contact__heading { text-align: right; color: var(--green); margin: 11px 0 5px; }
  .contact__row {
    display: flex; justify-content: space-between; margin: 0 0 6px; line-height: 15px;
  }
  .contact__label { color: var(--blue); }

  .band {
    position: absolute; left: 0; right: 0; top: 264px; height: 11px; display: flex;
  }
  .band__grey { width: 144px; background: var(--band-grey); }
  .band__green { flex: 1; background: var(--green); }
</style>
</head>
<body>
<main class="sheet">

  <section class="card card--front">
    <div class="brand">
      <span class="brand__square"></span>
      <span class="brand__name">HALDEN GRUPPE GmbH</span>
    </div>
  </section>

  <section class="card card--back card--mira">
    <div class="brand brand--small">
      <span class="brand__square"></span>
      <span class="brand__name">HALDEN GRUPPE</span>
    </div>
    <div class="divider"></div>
    <div class="person">
      <p class="person__name">Mira Halden</p>
      <p class="person__role">Geschäftsführer</p>
    </div>
    <div class="contact">
      <p class="contact__address">Lindenweg 12 | 10115 Berlin</p>
      <p class="contact__heading">Kontakt</p>
      <p class="contact__row"><span class="contact__label">Telefon:</span><span>+49 030 555 01 234</span></p>
      <p class="contact__row"><span class="contact__label">Telefax:</span><span>+49 030 555 01 234</span></p>
      <p class="contact__row"><span class="contact__label">E-Mail:</span><span>Halden@HaldenGruppe.de</span></p>
    </div>
    <div class="band"><span class="band__grey"></span><span class="band__green"></span></div>
  </section>

  <section class="card card--back card--selma">
    <div class="brand brand--small">
      <span class="brand__square"></span>
      <span class="brand__name">HALDEN GRUPPE</span>
    </div>
    <div class="divider"></div>
    <div class="person">
      <p class="person__name">Selma Arndt</p>
      <p class="person__role">Geschäftsführung</p>
    </div>
    <div class="contact">
      <p class="contact__address">Lindenweg 12 | 10115 Berlin</p>
      <p class="contact__heading">Kontakt</p>
      <p class="contact__row"><span class="contact__label">Telefon:</span><span>+49 030 555 01 234</span></p>
      <p class="contact__row"><span class="contact__label">Telefax:</span><span>+49 030 555 01 234</span></p>
      <p class="contact__row"><span class="contact__label">E-Mail:</span><span>Arndt@HaldenGruppe.de</span></p>
    </div>
    <div class="band"><span class="band__grey"></span><span class="band__green"></span></div>
  </section>

</main>
</body>
</html>
```